Logo for Sushi Mareta
Sushi Mareta
Project: Logo for Sushi Mareta
Logo for Sushi Mareta - Food
Creative Brief
Simple
2843 Linwell Avenue New York, NY 10241
sushimaretanyc@pondmail.example
My vision is to have a business card where on the back side is our logo and front side is our restaurant information with our logo be in the background.

```html
<!DOCTYPE html>
<html lang="en">
<head>
<meta charset="utf-8">
<title>Sushi Mareta — Stationery</title>
<link href="https://fonts.googleapis.com/css2?family=Open+Sans:wght@400;600;800&display=swap" rel="stylesheet">
<style>
  :root{
    --bg:#e9e9e9;
    --paper:#ffffff;
    --ink:#333333;
    --muted:#8a8a8a;
    --red:#e0211f;
    --black:#111111;
    --faint:#fbe9e4;
  }
  *{box-sizing:border-box;margin:0;padding:0}
  html,body{width:1200px;height:881px;overflow:hidden}
  body{background:var(--bg);font-family:"Open Sans",Arial,sans-serif;color:var(--ink);position:relative}
  .piece{position:absolute;background:var(--paper)}
  .brand{display:flex;align-items:center;gap:6px;font-weight:800;color:var(--red);text-transform:uppercase;letter-spacing:.5px}
  .brand .dot{border-radius:50%;background:var(--red);flex:none}

  /* business card front */
  .card-front{left:103px;top:149px;width:240px;height:144px;border-bottom:4px solid var(--red)}
  .card-front .brand{position:absolute;left:14px;top:14px;font-size:10px}
  .card-front .brand .dot{width:14px;height:14px}
  .card-front .name{position:absolute;left:14px;top:46px;font-size:10px;font-weight:800;color:var(--red);text-transform:uppercase}
  .card-front .role{position:absolute;left:14px;top:60px;font-size:6px;color:var(--muted)}
  .card-front .rule{position:absolute;left:14px;right:14px;top:72px;border-top:1px solid #e3e3e3}
  .card-front .contacts{position:absolute;left:14px;top:80px;font-size:5.5px;line-height:9px;color:var(--ink);list-style:none}
  .card-front .contacts li::before{content:"";display:inline-block;width:4px;height:4px;border-radius:50%;background:var(--red);margin-right:4px;vertical-align:middle}
  .card-front .address{position:absolute;right:14px;top:98px;font-size:5.5px;line-height:9px;text-align:right;width:70px}

  /* business card back */
  .card-back{left:355px;top:149px;width:226px;height:144px;background:var(--black);border-bottom:4px solid var(--red)}
  .card-back .pattern{position:absolute;inset:0;background:linear-gradient(160deg,#2a2a2a 0%,#151515 55%,#0a0a0a 100%)}
  .card-back .brand{position:absolute;right:14px;bottom:14px;font-size:7px}
  .card-back .brand .dot{width:10px;height:10px}

  /* envelope front */
  .envelope-front{left:103px;top:312px;width:480px;height:216px;border-bottom:4px solid var(--red)}
  .envelope-front .brand{position:absolute;left:12px;top:12px;font-size:12px}
  .envelope-front .brand .dot{width:16px;height:16px}
  .envelope-front .address{position:absolute;left:12px;top:44px;font-size:7px;line-height:11px;width:120px}

  /* envelope back */
  .envelope-back{left:103px;top:564px;width:480px;height:216px;overflow:hidden}
  .envelope-back svg{position:absolute;inset:0}
  .envelope-back .brand{position:absolute;left:0;right:0;top:22px;justify-content:center;font-size:9px}
  .envelope-back .brand .dot{width:13px;height:13px}

  /* letterhead */
  .letterhead{left:605px;top:67px;width:499px;height:718px;border-bottom:5px solid var(--red)}
  .letterhead .brand{position:absolute;left:40px;top:38px;font-size:13px}
  .letterhead .brand .dot{width:20px;height:20px}
  .letterhead .address{position:absolute;left:353px;top:26px;font-size:6.5px;line-height:10px;width:130px}
  .letterhead .contacts{position:absolute;left:353px;top:48px;font-size:6.5px;line-height:10px;list-style:none}
  .letterhead .contacts li::before{content:"";display:inline-block;width:4px;height:4px;border-radius:50%;background:var(--red);margin-right:5px;vertical-align:middle}
  .letterhead .watermark{position:absolute;left:50%;top:175px;transform:translateX(-50%);width:240px;height:240px;border-radius:50%;border:10px solid var(--faint);display:flex;align-items:center;justify-content:center;font-weight:800;font-size:22px;color:var(--faint);text-transform:uppercase}
</style>
</head>
<body>

<section class="piece card-front">
  <div class="brand"><span class="dot"></span>Sushi Mareta</div>
  <p class="name">Sushi Mareta</p>
  <p class="role">Owner</p>
  <div class="rule"></div>
  <ul class="contacts">
    <li>212 555 0147</li>
    <li>212 555 0182</li>
    <li>sushimaretanyc@pondmail.example</li>
    <li>www.sushimaretanyc.example</li>
  </ul>
  <p class="address">2843 Linwell Avenue New York, NY 10241</p>
</section>

<section class="piece card-back">
  <div class="pattern" role="img" aria-label="Dark repeating pattern of the restaurant emblem"></div>
  <div class="brand"><span class="dot"></span>Sushi Mareta</div>
</section>

<section class="piece envelope-front">
  <div class="brand"><span class="dot"></span>Sushi Mareta</div>
  <p class="address">2843 Linwell Avenue New York, NY 10241</p>
</section>

<section class="piece envelope-back">
  <svg width="480" height="216" viewBox="0 0 480 216">
    <path d="M0 0H480V62L430 72H50L0 62Z" fill="var(--black)"/>
    <line x1="0" y1="64" x2="50" y2="74" stroke="#dddddd"/>
    <line x1="480" y1="64" x2="430" y2="74" stroke="#dddddd"/>
  </svg>
  <div class="brand"><span class="dot"></span>Sushi Mareta</div>
</section>

<section class="piece letterhead">
  <div class="brand"><span class="dot"></span>Sushi Mareta</div>
  <p class="address">2843 Linwell Avenue<br>New York, NY 10241</p>
  <ul class="contacts">
    <li>212 555 0147</li>
    <li>212 555 0182</li>
    <li>sushimaretanyc@pondmail.example</li>
    <li>www.sushimaretanyc.example</li>
  </ul>
  <div class="watermark">Sushi Mareta</div>
</section>

</body>
</html>
```